Building company business card

Design and print business cards for BREVOTA PTY LTD.
A residantial homes building company.
Pixel Forge already designed the company Logo.

```html
<!DOCTYPE html>
<html lang="en">
<head>
<meta charset="utf-8">
<title>BREVOTA PTY LTD – Business Card</title>
<link rel="stylesheet" href="https://fonts.googleapis.com/css2?family=Bebas+Neue&family=Barlow:wght@400;500&display=swap">
<style>
  :root {
    --backdrop: #2b2b2b;
    --gold-deep: #8a5716;
    --gold-mid: #b98a3a;
    --gold-light: #dcb96a;
    --navy: #0f1f5e;
    --paper: #f1f1f1;
    --paper-shade: #e2e2e2;
    --front-text: #ededed;
  }
  * { margin: 0; padding: 0; box-sizing: border-box; }
  html, body { width: 1200px; height: 1138px; overflow: hidden; }
  body { background: var(--backdrop); position: relative; font-family: "Barlow", sans-serif; }

  .card { position: absolute; border-radius: 16px; overflow: hidden; }

  .card-front {
    left: 274px; top: 186px; width: 624px; height: 376px;
    background: linear-gradient(100deg, var(--gold-deep) 0%, var(--gold-mid) 40%, var(--gold-light) 100%);
  }
  .front-name {
    position: absolute; left: 0; right: 0; top: 188px; transform: translateY(-50%);
    text-align: center; font-family: "Bebas Neue", sans-serif;
    font-size: 104px; line-height: 1; color: var(--front-text); letter-spacing: 1px;
  }
  .front-web {
    position: absolute; left: 0; right: 0; top: 330px; margin-left: 12px;
    text-align: center; font-size: 16px; line-height: 20px; color: var(--front-text);
    letter-spacing: 0.95em; opacity: .9;
  }

  .card-back {
    left: 276px; top: 608px; width: 618px; height: 374px;
    background: linear-gradient(180deg, var(--paper) 0%, var(--paper-shade) 100%);
  }
  .back-band {
    position: absolute; left: 0; right: 0; bottom: 0; height: 16px;
    background: linear-gradient(90deg, var(--gold-deep), var(--gold-light));
  }
  .back-brand {
    position: absolute; left: 54px; top: 152px;
    font-family: "Bebas Neue", sans-serif; font-size: 70px; line-height: 1;
    color: var(--navy); letter-spacing: 1px;
  }
  .details { position: absolute; left: 302px; top: 80px; color: var(--navy); }
  .company { font-family: "Bebas Neue", sans-serif; font-size: 50px; line-height: 1; letter-spacing: 1.5px; font-weight: 400; }
  .person { font-family: "Bebas Neue", sans-serif; font-size: 29px; line-height: 1; margin-top: 18px; letter-spacing: .5px; }
  .role { font-size: 16px; line-height: 1; margin-top: 4px; }
  .ids { font-size: 16px; margin-top: 16px; line-height: 1; font-weight: 500; }
  .contacts { list-style: none; margin-top: 9px; }
  .contacts li { display: flex; align-items: center; font-size: 16px; line-height: 22.5px; font-weight: 500; }
  .contacts svg { width: 14px; height: 14px; margin-right: 14px; fill: var(--gold-mid); flex: none; }
</style>
</head>
<body>
  <section class="card card-front">
    <div class="front-name">BREVOTA</div>
    <div class="front-web">www.brevota-pl.com</div>
  </section>

  <section class="card card-back">
    <div class="back-brand">BREVOTA</div>
    <div class="details">
      <h1 class="company">BREVOTA PTY LTD</h1>
      <p class="person">DORIAN (DAN) KESSLER</p>
      <p class="role">Director</p>
      <p class="ids">ABN-48 210 736 594 &nbsp;|&nbsp; CDB-U 58160</p>
      <ul class="contacts">
        <li><svg viewBox="0 0 16 16" aria-hidden="true"><path d="M1 3h14v10H1z M1 3l7 6 7-6" fill="none" stroke="#b98a3a" stroke-width="1.6"/></svg>dkr@brevota-pl.com</li>
        <li><svg viewBox="0 0 16 16" aria-hidden="true"><path d="M3 1.5l3 .5 1 3.5-2 1.5c1 2 2.5 3.5 4.5 4.5l1.5-2 3.5 1 .5 3c-7 1-13-5-12-12z"/></svg>0412 555 083 &amp; 0438 555 216</li>
        <li><svg viewBox="0 0 16 16" aria-hidden="true"><path d="M8 0.5a5.5 5.5 0 0 0-5.5 5.5c0 4 5.5 9.5 5.5 9.5s5.5-5.5 5.5-9.5A5.5 5.5 0 0 0 8 .5zm0 3a2.5 2.5 0 1 1 0 5 2.5 2.5 0 0 1 0-5z"/></svg>PO Box 482, Kewton North, VIC 3199</li>
      </ul>
    </div>
    <div class="back-band"></div>
  </section>
</body>
</html>
```